The Corvanta Group's website for high impact furniture promotions

I am looking for a simple website. we are a promotional company that runs events for furniture stores to increase sales for short periods of time. i would like the website to have about 4 areas to explain our company. I would like it to be simple and user friendly. I would like a link to chatterbook and a contact section. I am attaching our logo that i would like somewhere large or possibly in the backround. I am open to different color schemes. I would like to convey fast paced, modern, reliable. I am open to all different styles and look forward to seeing whats out there. we are looking for a quick turn around, so if we see one that we like quick, we will pick that one thanks
Updates
Project Deadline Extended
Reason: looking for some really creative designs and want to give a fair amount of time to produce
Target Market(s)
Retail Furniture store owners
Industry/Entity Type
It Company
Number of Pages Required
1 page
Colors
Designer to choose colors to be used in the design.
Look and feel
Each slider illustrates characteristics of the customer's brand and the style your logo design should communicate.

```html
<!DOCTYPE html>
<html lang="en">
<head>
<meta charset="utf-8">
<title>The Corvanta Group — High Impact Furniture Promotions</title>
<link href="https://fonts.googleapis.com/css2?family=Montserrat:wght@400;700&family=Raleway:wght@400;500;600&display=swap" rel="stylesheet">
<style>
:root{
  --cream:#f7f7d6;
  --pale-olive:#ece9a3;
  --olive:#7f801f;
  --olive-dark:#66650f;
  --footer:#8d8f33;
  --brown:#8a5a2c;
  --ink:#222;
  --muted:#8a8a8a;
  --card:#f4f4f4;
}
*{box-sizing:border-box;margin:0;padding:0}
html,body{width:1200px;height:1120px;overflow:hidden;background:#fff}
body{position:relative;font-family:'Raleway',sans-serif;color:var(--ink)}
.abs{position:absolute}
.photo{position:absolute}

/* hero */
.hero{left:354px;top:0;width:492px;height:240px;background:var(--cream)}
.brand{position:absolute;text-align:center;font-family:'Montserrat',sans-serif}
.brand-dot{display:block;margin:0 auto;border-radius:50%;background:var(--brown)}
.hero .brand{left:0;right:0;top:8px}
.hero .brand-dot{width:26px;height:26px}
.hero .brand-name{font-size:8px;letter-spacing:1.5px;color:var(--brown);margin-top:5px}
.welcome{left:64px;top:104px;font-family:'Montserrat',sans-serif;font-size:10px;letter-spacing:1px}
.hero-title{left:64px;top:120px;font-family:'Montserrat',sans-serif;font-weight:700;font-size:15px;letter-spacing:1px;color:var(--olive)}
.hero-copy{left:64px;top:146px;width:152px;font-family:'Montserrat',sans-serif;font-size:4.6px;line-height:5.4px}
.dining{left:260px;top:92px;width:162px;height:110px;border-radius:6px;background:radial-gradient(ellipse at center,#d8cbb4 0%,#5a3b26 55%,rgba(247,247,214,0) 75%)}

/* features */
.feature-block{left:417px;top:278px;width:241px;height:128px;background:var(--pale-olive)}
.chair-red{left:440px;top:282px;width:114px;height:120px;background:radial-gradient(ellipse at center,#d9735a 0%,#a5432f 45%,rgba(236,233,163,0) 72%)}
.chair-frame{left:440px;top:284px}
.feature-block-2{left:668px;top:358px;width:114px;height:140px;background:var(--pale-olive)}
.chair-blue{left:690px;top:370px;width:86px;height:108px;background:radial-gradient(ellipse at center,#3d5676 0%,#2d4260 40%,rgba(236,233,163,0) 72%)}
.arrivals{left:417px;top:417px;width:85px;height:81px;background:linear-gradient(160deg,#8a8a3a,#6f7028)}
.arrivals span{position:absolute;left:0;right:0;top:35px;text-align:center;color:#fff;font-weight:600;font-size:10px}
.f-heading{font-size:9.5px;font-weight:500}
.f-copy{font-size:4.6px;line-height:7px}
.h1{left:602px;top:293px}
.c1{left:602px;top:311px;width:174px}
.h2{left:500px;top:428px;width:186px;text-align:right}
.c2{left:512px;top:446px;width:174px;text-align:right}

/* newsletter */
.newsletter{left:354px;top:537px;width:492px;height:165px;background:var(--cream)}
.desk{left:417px;top:570px;width:153px;height:88px;background:radial-gradient(ellipse at 50% 65%,#6a3b1f 0%,#4a2a17 45%,rgba(247,247,214,0) 72%)}
.dot-sm{position:absolute;width:15px;height:15px;border-radius:50%;background:var(--brown)}
.news-title{left:606px;top:596px;width:176px;text-align:center;font-size:9px;letter-spacing:.3px}
.news-copy{left:606px;top:613px;width:176px;text-align:center;font-size:4.3px;line-height:7px}
.email{left:606px;top:642px;width:140px;height:13px;border:1px solid #9a9a55;background:#fff;font-size:3.8px;color:#999;padding:4px 5px}
.submit{left:746px;top:642px;width:36px;height:13px;background:var(--olive-dark);color:#fff;font-size:4px;text-align:center;line-height:13px}

/* posts */
.posts-title{left:0;width:1200px;top:759px;text-align:center;font-size:9px;letter-spacing:.3px}
.card{top:791px;width:120px;height:142px;background:var(--card);border:1px solid #e8e8e8;text-align:center}
.card .img{position:absolute;left:5px;top:5px;width:109px;height:74px}
.card h3{position:absolute;left:0;right:0;top:86px;font-size:6.5px;font-weight:500}
.card p{position:absolute;left:14px;right:14px;top:98px;font-size:3.8px;line-height:5.4px}
.card small{position:absolute;left:0;right:0;top:126px;font-size:4px;color:var(--muted)}
.nav-btn{width:20px;height:20px;border-radius:50%;background:#fff;border:1px solid #e2e2e2;top:859px}

/* footer */
.footer{left:354px;top:970px;width:492px;height:127px;background:var(--footer)}
.footer .brand{left:0;right:0;top:13px}
.footer .brand-dot{width:20px;height:20px}
.footer .brand-name{font-size:7px;letter-spacing:1.2px;color:#fff;margin-top:4px}
.rule{height:1px;background:rgba(255,255,255,.45)}
.social{left:0;right:0;top:77px;text-align:center;font-size:7px;color:#fff;font-weight:600;word-spacing:6px}
.copyright{left:0;right:0;top:113px;text-align:center;font-size:4.5px;color:#fff;letter-spacing:.3px}
</style>
</head>
<body>

<section class="abs hero" aria-label="Welcome">
  <div class="brand"><span class="brand-dot"></span><div class="brand-name">THE CORVANTA GROUP</div></div>
  <svg class="abs" style="left:26px;top:128px" width="22" height="8" viewBox="0 0 22 8"><path d="M21 4H2M5 1L1.5 4 5 7" stroke="#7f801f" fill="none" stroke-width="1.2"/></svg>
  <svg class="abs" style="left:448px;top:128px" width="22" height="8" viewBox="0 0 22 8"><path d="M1 4h19M17 1l3.5 3L17 7" stroke="#7f801f" fill="none" stroke-width="1.2"/></svg>
  <p class="abs welcome">Welcome To</p>
  <h1 class="abs hero-title">Corvanta Group</h1>
  <p class="abs hero-copy">Lorem Ipsum is simply dummy text of the printing and typesetting industry. Lorem Ipsum has been the industry's standard dummy text ever since the 1500s, when an unknown printer took a galley of type and scrambled it to make a type specimen book.</p>
  <svg class="abs" style="left:64px;top:178px" width="24" height="6" viewBox="0 0 24 6"><path d="M0 3h22M19 .5l3 2.5-3 2.5" stroke="#7f801f" fill="none"/></svg>
  <div class="photo dining" role="img" aria-label="Photo of a marble dining table with dark wooden chairs"></div>
</section>

<div class="abs feature-block"></div>
<svg class="abs chair-frame" width="114" height="112" viewBox="0 0 114 112"><polygon points="33,6 114,28 88,110 4,84" fill="none" stroke="#7f801f" stroke-width="1.6"/></svg>
<div class="photo chair-red" role="img" aria-label="Photo of a coral tufted armchair"></div>
<h2 class="abs f-heading h1">Your Heading Goes Here</h2>
<p class="abs f-copy c1">Lorem Ipsum is simply dummy text of the printing and typesetting industry. Lorem Ipsum has been the industry's standard dummy text ever since the 1500s, when an unknown printer took a galley of type and scrambled it to make a type specimen book.</p>
<svg class="abs" style="left:602px;top:347px" width="24" height="6" viewBox="0 0 24 6"><path d="M0 3h22M19 .5l3 2.5-3 2.5" stroke="#7f801f" fill="none"/></svg>

<div class="abs feature-block-2"></div>
<div class="photo chair-blue" role="img" aria-label="Photo of a navy plastic chair on chrome legs"></div>
<div class="photo arrivals" role="img" aria-label="Photo of a furnished dining room with an olive tint"><span>New Arrivals</span></div>
<h2 class="abs f-heading h2">Your Heading Goes Here</h2>
<p class="abs f-copy c2">Lorem Ipsum is simply dummy text of the printing and typesetting industry. Lorem Ipsum has been the industry's standard dummy text ever since the 1500s, when an unknown printer took a galley of type and scrambled it to make a type specimen book.</p>
<svg class="abs" style="left:662px;top:480px" width="24" height="6" viewBox="0 0 24 6"><path d="M24 3H2M5 .5L2 3l3 2.5" stroke="#7f801f" fill="none"/></svg>

<section class="abs newsletter" aria-label="Newsletter"></section>
<div class="photo desk" role="img" aria-label="Photo of a dark wood corner desk with lamp and monitor"></div>
<span class="dot-sm" style="left:687px;top:576px"></span>
<h2 class="abs news-title">SIGN UP NEWSLETTER</h2>
<p class="abs news-copy">Lorem Ipsum is simply dummy text of the printing and typesetting industry. Lorem Ipsum has been the industry's standard dummy text ever since the 1500s.</p>
<div class="abs email">Enter Your Email Address</div>
<div class="abs submit">Submit</div>

<span class="dot-sm" style="left:592px;top:735px"></span>
<h2 class="abs posts-title">RECENT POSTS</h2>

<article class="abs card" style="left:414px">
  <div class="photo img" role="img" aria-label="Photo of a dining room with wooden table and pendant lamps" style="background:linear-gradient(180deg,#e9e4dc,#6b4a36)"></div>
  <h3>Your Heading Goes Here</h3>
  <p>Lorem Ipsum is simply dummy text of the printing and typesetting industry. Lorem Ipsum has been the industry's standard dummy text ever since the 1500s.</p>
  <small>Your Heading</small>
</article>
<article class="abs card" style="left:540px">
  <div class="photo img" role="img" aria-label="Photo of a mint lounge with black sofa and white chairs" style="background:linear-gradient(180deg,#8fd1bd,#2e3a3a)"></div>
  <h3>Your Heading Goes Here</h3>
  <p>Lorem Ipsum is simply dummy text of the printing and typesetting industry. Lorem Ipsum has been the industry's standard dummy text ever since the 1500s.</p>
  <small>Your Heading</small>
</article>
<article class="abs card" style="left:666px">
  <div class="photo img" role="img" aria-label="Photo of a warm living room with fireplace and armchairs" style="background:linear-gradient(180deg,#4a2e1e,#c58a4a)"></div>
  <h3>Your Heading Goes Here</h3>
  <p>Lorem Ipsum is simply dummy text of the printing and typesetting industry. Lorem Ipsum has been the industry's standard dummy text ever since the 1500s.</p>
  <small>Your Heading</small>
</article>
<svg class="abs nav-btn" style="left:402px" viewBox="0 0 20 20"><path d="M11 7l-3 3 3 3" stroke="#aaa" fill="none"/></svg>
<svg class="abs nav-btn" style="left:776px" viewBox="0 0 20 20"><path d="M9 7l3 3-3 3" stroke="#aaa" fill="none"/></svg>

<footer class="abs footer">
  <div class="brand"><span class="brand-dot"></span><div class="brand-name">THE CORVANTA GROUP</div></div>
  <div class="abs rule" style="left:171px;width:151px;top:66px"></div>
  <nav class="abs social">chatterbook Flitter Pinboardly Linkwell Orbitplus</nav>
  <div class="abs rule" style="left:87px;width:315px;top:105px"></div>
  <p class="abs copyright">Copyright © 2017 Corvanta Group - All Rights Reserved.</p>
</footer>

</body>
</html>
```